KW Sports & Remedial Massage needs a new logo & business card design

The design is for my Sports and remedial massage business. My business is aimed at everyone who has a muscle ache or injury so not just sports related. I need a design which is sharp, clear and professional. No greens, or pastel colours or floral/girly designs. Perhaps just a Navy background and white text or other way around or perhaps grey. I want to make it clear that I treat everyone and not just sporty people.

Target Market(s)

People with muscle aches or sports injuries

Industry/Entity Type

Health And Wellness

Contact Information for Business Card

It needs to also include the following:
Name: Marion Kebbell
Mobile No: 07432 519 268
Email: marionkebbell@postvane.com
Qualifications: Dip SM, Dip SRM

Logo Text

KW Sports & Remedial Massage

Font styles to use
Serif
Other font styles liked:
• Tahoma, Verdana

Colors
5c5c5c
7f7f7f
9d9d9d
0255a3
3176b5
85abd2

Requirements
Must have
• I was thinking of a few simple people figures at the bottom of the card to highlight this i.e. a gardener, musician mixed in with a cyclist and tennis player.
Should not have
• Anything which indicates beauty therapy or relaxing. I am there to get rid of aches and pains and often to give rehab to certain injuries.

```html
<!DOCTYPE html>
<html lang="en">
<head>
<meta charset="utf-8">
<title>Marion Kebbell – Business Card</title>
<link rel="stylesheet" href="https://fonts.googleapis.com/css2?family=Questrial&family=Open+Sans:wght@400;700&display=swap">
<style>
  :root {
    --stage: #2b2b2d;
    --navy-deep: #1c1a55;
    --navy: #28266f;
    --navy-ink: #24225e;
    --paper: #ffffff;
    --grey-text: #6a6a6a;
    --soft-white: #e6e6f2;
  }
  * { margin: 0; padding: 0; box-sizing: border-box; }
  html, body {
    width: 1200px; height: 900px; overflow: hidden;
    background: var(--stage);
  }
  .stage { position: relative; width: 1200px; height: 900px; }
  .card {
    position: absolute; left: 267px; width: 666px; height: 380px;
    box-shadow: 0 10px 30px rgba(0,0,0,.45);
  }
  /* front */
  .card--front {
    top: 50px;
    background: linear-gradient(100deg, var(--navy-deep) 0%, var(--navy) 70%, #35338a 100%);
  }
  .front-name {
    position: absolute; right: 48px; bottom: 88px; text-align: right;
    color: var(--soft-white);
    font-family: "Questrial", sans-serif;
  }
  .front-name__title { font-size: 40px; letter-spacing: .5px; line-height: 1; }
  .front-name__tagline { font-size: 13px; margin-top: 6px; letter-spacing: .3px; }
  /* back */
  .card--back { top: 470px; background: var(--paper); }
  .brand {
    position: absolute; top: 26px; left: 0; right: 0; text-align: center;
    color: var(--navy-ink);
    font-family: "Questrial", sans-serif;
  }
  .brand__mark {
    display: block; margin: 0 auto; width: 96px; height: 80px;
    background: var(--navy-ink);
  }
  .brand__name { font-size: 40px; line-height: 1; margin-top: 8px; }
  .brand__tagline { font-size: 13px; margin-top: 6px; }
  .contact {
    position: absolute; left: 48px; bottom: 30px;
    font-family: "Open Sans", sans-serif;
  }
  .contact__name { font-size: 26px; font-weight: 700; color: var(--navy-ink); line-height: 1.1; }
  .contact__quals { font-size: 20px; color: var(--grey-text); margin-top: 2px; line-height: 1.3; }
  .contact__list { list-style: none; margin-top: 10px; }
  .contact__item {
    display: flex; align-items: center; gap: 14px;
    font-size: 18px; color: var(--grey-text); line-height: 1.6;
  }
  .contact__icon { width: 18px; height: 18px; flex: none; }
  .contact__at { font-weight: 700; color: var(--navy-ink); font-size: 19px; width: 18px; text-align: center; }
</style>
</head>
<body>
<main class="stage">
  <section class="card card--front">
    <div class="front-name">
      <p class="front-name__title">Marion Kebbell</p>
      <p class="front-name__tagline">Sports and remedial massage business</p>
    </div>
  </section>

  <section class="card card--back">
    <header class="brand">
      <span class="brand__mark" aria-hidden="true"></span>
      <p class="brand__name">Marion Kebbell</p>
      <p class="brand__tagline">Sports and remedial massage business</p>
    </header>

    <div class="contact">
      <p class="contact__name">Marion Kebbell</p>
      <p class="contact__quals">Dip SM, Dip SRM</p>
      <ul class="contact__list">
        <li class="contact__item">
          <svg class="contact__icon" viewBox="0 0 24 24" aria-hidden="true">
            <path d="M6.6 10.8a15 15 0 0 0 6.6 6.6l2.2-2.2a1 1 0 0 1 1-.25 11.4 11.4 0 0 0 3.6.57 1 1 0 0 1 1 1V20a1 1 0 0 1-1 1A17 17 0 0 1 3 4a1 1 0 0 1 1-1h3.5a1 1 0 0 1 1 1c0 1.25.2 2.45.57 3.57a1 1 0 0 1-.25 1z" fill="var(--navy-ink)"/>
          </svg>
          <span>07432 519 268</span>
        </li>
        <li class="contact__item">
          <span class="contact__at" aria-hidden="true">@</span>
          <span>marionkebbell@postvane.com</span>
        </li>
      </ul>
    </div>
  </section>
</main>
</body>
</html>
```